CBD Syrup Label 4" Wide, 2" Tall

I am looking for a fun modern supplement lab for a new CBD infused syrup. I have attached a few examples of some I like from other companies. Company name is Vorpen. Logo is attached

Target Market(s)

Younger males

Font styles to use
Serif
Sans Serif

Colors

Designer to choose colors to be used in the design.

Requirements
Must have
• Logo centered. Each label a different color. Flavors will be descided later. Looking for colors or maybe fruit flavor ideas.

```html
<!DOCTYPE html>
<html lang="en">
<head>
<meta charset="utf-8">
<title>Vorpen Orange Punch CBD Syrup Label</title>
<link href="https://fonts.googleapis.com/css2?family=Lato:wght@400;700;900&family=Oswald:wght@300;400&display=swap" rel="stylesheet">
<style>
  :root {
    --page-bg: #e4e4e4;
    --label-bg: #ffffff;
    --band: #f5a300;
    --accent-text: #e39c17;
    --ink: #1c1c1c;
    --leaf: #3f9a3a;
    --fruit: #f3b52a;
  }
  * { margin: 0; padding: 0; box-sizing: border-box; }
  html, body { width: 1200px; height: 900px; overflow: hidden; }
  body {
    background: radial-gradient(circle at 50% 40%, #f4f4f4, var(--page-bg));
    font-family: "Lato", sans-serif;
    color: var(--ink);
    position: relative;
  }
  .label {
    position: absolute; left: 40px; top: 203px;
    width: 1120px; height: 494px;
    background: var(--label-bg);
    box-shadow: 0 18px 24px -14px rgba(0,0,0,.35);
  }
  .band { position: absolute; left: 0; width: 100%; background: var(--band); }
  .band--top { top: 0; height: 25px; }
  .band--bottom { bottom: 0; height: 19px; }

  .info-column { position: absolute; left: 32px; top: 60px; width: 330px; font-size: 15.5px; line-height: 20px; }
  .info-column p + p { margin-top: 20px; }
  .badges { display: flex; gap: 30px; margin-top: 38px; }
  .badge { width: 56px; height: 56px; border-radius: 50%; border: 2px solid var(--ink); }
  .distributor { margin-top: 34px; }
  .distributor strong { font-weight: 700; }

  .front-panel { position: absolute; left: 392px; top: 0; width: 340px; height: 100%; text-align: center; }
  .flavor, .product-type, .volume {
    font-family: "Oswald", sans-serif; font-weight: 300;
    color: var(--accent-text); letter-spacing: 4px; position: absolute; width: 100%;
  }
  .flavor { top: 58px; font-size: 20px; }
  .art-top { position: absolute; left: 10px; top: 92px; width: 320px; height: 96px; }
  .brand-name {
    position: absolute; top: 178px; width: 100%;
    font-family: "Lato", sans-serif; font-weight: 900;
    font-size: 112px; line-height: 1; letter-spacing: -4px; color: var(--ink);
  }
  .art-bottom { position: absolute; left: 20px; top: 306px; width: 300px; height: 72px; }
  .product-type { top: 387px; font-size: 19px; }
  .remedy {
    position: absolute; top: 414px; width: 100%;
    font-family: "Oswald", sans-serif; font-weight: 300;
    font-size: 19px; letter-spacing: 4px; color: var(--ink);
  }
  .volume { top: 442px; font-size: 19px; letter-spacing: 3px; }

  .facts {
    position: absolute; left: 824px; top: 41px; width: 262px; height: 311px;
    border: 2px solid var(--ink); padding: 4px 8px; font-size: 11px; line-height: 14px;
  }
  .facts h2 { font-size: 20px; font-weight: 700; line-height: 22px; }
  .facts hr { border: none; border-top: 1.5px solid var(--ink); margin: 6px 0 6px; }
  .facts h3 { font-size: 11px; font-weight: 700; }
  .facts .row { display: flex; gap: 10px; }
  .facts .row span:first-child { width: 102px; }
  .facts .block { margin-top: 10px; }
  .disclaimer { position: absolute; left: 824px; top: 376px; width: 262px; font-size: 11px; line-height: 14px; }
</style>
</head>
<body>
  <main class="label">
    <div class="band band--top"></div>

    <section class="info-column">
      <p>Full Spectrum Hemp Extract formula is a daily supplement great for Exercise Recovery, Inflammation, Aches and Pains, General Wellness, and Brain Health</p>
      <p>These Statements have not been evaluated by the FDA.&nbsp; This product is not intended to diagnose, treat, cure, or prevent any disease.</p>
      <div class="badges">
        <div class="badge"></div>
        <div class="badge"></div>
      </div>
      <p class="distributor"><strong>Distributed by:</strong><br>
        Vorpen Nutraceuticals Hemp<br>
        Millbrook, PA. 18022<br>
        info@vorpen.com<br>
        www.vorpen.com</p>
    </section>

    <section class="front-panel">
      <div class="flavor">ORANGE PUNCH</div>
      <svg class="art-top" role="img" aria-label="Orange fruit with leaf and orange slice among green hemp leaves" viewBox="0 0 320 96">
        <defs>
          <linearGradient id="artTopFill" x1="0" y1="0" x2="1" y2="0">
            <stop offset="0" stop-color="#4ea845"/>
            <stop offset=".5" stop-color="#f3b52a"/>
            <stop offset="1" stop-color="#4ea845"/>
          </linearGradient>
        </defs>
        <rect width="320" height="96" rx="6" fill="url(#artTopFill)" opacity=".85"/>
      </svg>
      <div class="brand-name">Vorpen</div>
      <svg class="art-bottom" role="img" aria-label="Fan of green hemp leaves" viewBox="0 0 300 72">
        <rect width="300" height="72" rx="6" fill="#3f9a3a" opacity=".8"/>
      </svg>
      <div class="product-type">CBD INFUSED SYRUP</div>
      <div class="remedy">NATURAL SLEEP REMEDY</div>
      <div class="volume">4 fl.oz (108ml)</div>
    </section>

    <section class="facts">
      <h2>Supplemement Facts</h2>
      <div>Serving Size&nbsp; : 1 ml</div>
      <div>Serving Per Bottle : 30</div>
      <hr>
      <h3>Amount/Serving</h3>
      <div>% DailyValue</div>
      <div class="row"><span>Cannabidiol (CBD)</span><span>10 mg *</span></div>
      <div class="row"><span>Cannabigerol (CBG)</span><span>3.3 mg *</span></div>
      <hr>
      <div>*daily value not established</div>
      <div class="block">
        <h3>Other Ingredients</h3>
        <div>GRAS Food Grade Oil Extracts (Strawberry Flavoring, Lemonade flavoring) Oleic Acid, Avocado Oil, Coco Oil, Primrose Oil, USP Grade Natural Plant Terpenes (a-pinene, a-terpinene, b-caryophyllene, d3 carene, linalool, myrcene)</div>
      </div>
    </section>

    <p class="disclaimer">This product is not intended to diagnose, treat, cure or prevent any disease. These statements have not been evaluated by the Food &amp; Drug Administration.</p>

    <div class="band band--bottom"></div>
  </main>
</body>
</html>
```